Vintage poster/postcard for 2011 New Years Eve event with theme 'Velvet Lanterns'

I have had a major change of mind since the last brief due to my original requirements being too specific. I hope this new brief allows more scope for the designers and I am extending the deadline by 7 days.

For the first time my new business 'Larkmoor Galas' is planning an exciting, large scale New Years Eve fundraising event in Hobart Tasmania, Australia. The unique and eclectic theme of the party is 'Velvet Lanterns' (french for contemporary circus). I require a vintage style poster design (similar to a traditional french advertising poster) that can double as a postcard invitation so it must look good on a smaller scale as well.
Updates

Project Deadline Extended
Reason: My original brief was very specific and I now realise very limiting for the designers. I have changed my mind with the look I want for the vintage poster (more along the lines of the traditional french advertising posters of old) and therefore would like to allow designers extra time to submit a design. Thank you. Dena Voss Larkmoor Galas

Target Market(s)

25-50 yr old professionals prepared to pay premium price for a quality, fresh & fun NYE experience while giving to charity.

Industry/Entity Type

Advertising

Requirements
Must have
• - A heading that reads: Larkmoor Galas proudly presents
Velvet Lanterns
- Text that includes: 2011 New Years Eve Extravanaganza Saturday 31st December and find out more at "www.larkmoorgalas.example
- A strip left blank at the bottom to include my business logo and others sponsors
- Classic french vintage poster design
- - Plenty of colour but not too fluro
- Something that looks good enough to be framed or sent to a friend
Should not have
• - Picture of Eiffel Tower or any other specific French references
- Any animals

```html
<!DOCTYPE html>
<html lang="en">
<head>
<meta charset="utf-8">
<title>Velvet Lanterns – New Years Eve Extravanaganza</title>
<link rel="stylesheet" href="https://fonts.googleapis.com/css2?family=Montserrat:wght@600;700;800;900&display=swap">
<style>
  :root{
    --red:#c3172b;
    --red-deep:#7a0c16;
    --red-dark:#3d0508;
    --beige:#d8c79d;
    --beige-light:#ece0bf;
    --navy:#1d2738;
    --tan:#9c8c68;
    --cream:#f4f1e8;
  }
  html,body{margin:0;padding:0;overflow:hidden;background:var(--red-dark);}
  .poster{position:relative;width:816px;height:1200px;overflow:hidden;
    font-family:"Montserrat",Arial,sans-serif;text-transform:uppercase;}
  .backdrop{position:absolute;inset:0;}
  .line{position:absolute;margin:0;white-space:nowrap;line-height:1;
    transform:rotate(-10deg);transform-origin:left bottom;font-weight:900;}
  .band{padding:6px 18px 4px;}
  .presenter{left:23px;top:96px;font-size:28px;font-weight:800;color:var(--cream);letter-spacing:.5px;}
  .presenter .soft{color:var(--beige);text-transform:lowercase;}
  .title-top{left:-10px;top:182px;font-size:40px;color:var(--red);background:var(--cream);padding-left:40px;padding-right:60px;}
  .title-main{left:-10px;top:270px;font-size:104px;color:var(--navy);background:var(--cream);padding:8px 30px 4px 30px;letter-spacing:-3px;}
  .day{left:470px;top:392px;font-size:54px;color:var(--tan);background:var(--cream);padding:4px 14px 2px;}
  .date{left:410px;top:452px;font-size:48px;color:var(--cream);background:var(--tan);padding:6px 14px 2px;}
  .date sup{font-size:.55em;vertical-align:.55em;}
  .year{left:600px;top:490px;font-size:78px;color:var(--red);background:var(--cream);padding:4px 14px 0;}
  .event{left:380px;top:624px;font-size:36px;color:var(--red);background:var(--cream);padding:4px 14px 2px;}
  .headline{left:150px;top:716px;font-size:52px;color:var(--navy);background:var(--cream);padding:6px 16px 2px;letter-spacing:-1px;}
  .more-label{left:390px;top:890px;font-size:26px;font-weight:800;color:var(--cream);}
  .web{left:90px;top:985px;font-size:34px;color:var(--cream);letter-spacing:-.5px;}
  .web .accent{color:var(--red);}
</style>
</head>
<body>
<div class="poster">
  <svg class="backdrop" width="816" height="1200" viewBox="0 0 816 1200">
    <defs>
      <radialGradient id="redGlow" cx="50%" cy="40%" r="75%">
        <stop offset="0" stop-color="#d8223a"/>
        <stop offset="1" stop-color="#8e0f1c"/>
      </radialGradient>
      <linearGradient id="beigeBand" x1="0" y1="0" x2="1" y2="1">
        <stop offset="0" stop-color="#ece0bf"/>
        <stop offset="1" stop-color="#d8c79d"/>
      </linearGradient>
      <linearGradient id="maskTone" x1="0" y1="0" x2="1" y2="0">
        <stop offset="0" stop-color="#a8121f"/>
        <stop offset="1" stop-color="#5e0a12"/>
      </linearGradient>
      <linearGradient id="footTone" x1="0" y1="0" x2="0" y2="1">
        <stop offset="0" stop-color="#8a0f1b"/>
        <stop offset="1" stop-color="#3d0508"/>
      </linearGradient>
    </defs>
    <rect width="816" height="1200" fill="url(#redGlow)"/>
    <ellipse cx="420" cy="430" rx="640" ry="360" transform="rotate(-10 420 430)" fill="url(#beigeBand)"/>
    <ellipse cx="430" cy="470" rx="560" ry="250" transform="rotate(-10 430 470)" fill="var(--red)"/>
    <path role="img" aria-label="Stylised masquerade mask illustration in deep red" d="M0 560 C150 470 330 470 470 560 C420 700 300 790 160 800 C90 800 30 780 0 760 Z" fill="url(#maskTone)"/>
    <polygon points="0,1080 816,936 816,1200 0,1200" fill="url(#footTone)"/>
    <polygon points="0,870 816,726 816,936 0,1080" fill="var(--red-dark)"/>
  </svg>

  <p class="line presenter">Larkmoor Galas <span class="soft">proudly</span> presents</p>
  <h1 class="line title-top band">Velvet</h1>
  <h1 class="line title-main">Lanterns</h1>
  <p class="line day">Saturday</p>
  <p class="line date">31<sup>st</sup> December</p>
  <p class="line year">2011</p>
  <p class="line event">New Years Eve</p>
  <p class="line headline">Extravanaganza</p>
  <p class="line more-label">Find out more at</p>
  <p class="line web">www.<span class="accent">larkmoorgalas</span>.example</p>
</div>
</body>
</html>
```